Van/Car Signage

I'm looking for artwork designs for signwriting for our company cars & Vans. 1 x 2023 Velko Stratum Parowen & 1 x 2024 Holm Ravenette LWB Both are White. You can access our company details and product range at www.quillmereprovisionhaus.com.au - i have uploaded our logo.

```html
<!DOCTYPE html>
<html lang="en">
<head>
<meta charset="utf-8">
<title>Quillmere Provision Haus – Vehicle Signage</title>
<link rel="stylesheet" href="https://fonts.googleapis.com/css2?family=Montserrat:wght@600;700;800&display=swap">
<style>
  :root{
    --stage:#4d4d4d;
    --brand-blue:#1f72bb;
    --brand-red:#e8202a;
    --white:#ffffff;
    --photo-dark:#55585c;
    --photo-light:#b9b3a8;
  }
  *{margin:0;padding:0;box-sizing:border-box}
  html,body{width:1200px;height:1200px;overflow:hidden;background:var(--stage)}
  body{position:relative;font-family:"Montserrat",sans-serif}
  .panel{position:absolute;background:var(--white);overflow:hidden}
  .panel svg{position:absolute;inset:0;width:100%;height:100%}
  .side-left{left:122px;top:67px;width:952px;height:307px}
  .side-right{left:122px;top:404px;width:952px;height:307px}
  .side-right .graphics{transform:scaleX(-1)}
  .tailgate{left:123px;top:740px;width:953px;height:262px}
  .strip{left:122px;top:1032px;width:957px;height:90px;background:var(--brand-red);
    display:flex;align-items:center;justify-content:center}
  .contact{position:absolute;top:182px;transform:translateX(-50%);text-align:center;color:var(--brand-blue)}
  .side-left .contact{left:578px}
  .side-right .contact{left:354px}
  .brand-line{display:flex;align-items:center;justify-content:center;gap:6px;
    font-weight:700;font-size:15px;line-height:20px;color:var(--brand-blue);white-space:nowrap}
  .brand-dot{width:12px;height:12px;background:var(--brand-red)}
  .phone{margin-top:10px;font-weight:700;font-size:14px;line-height:16px;white-space:nowrap;
    display:flex;align-items:center;justify-content:center;gap:3px}
  .phone svg{position:static;width:9px;height:9px}
  .web{margin-top:7px;font-weight:700;font-size:6.4px;letter-spacing:.3px;white-space:nowrap}
  .tailgate .brand{position:absolute;left:150px;top:96px;width:300px;text-align:center}
  .tailgate .brand-dot{width:56px;height:56px;margin:0 auto 14px}
  .tailgate .brand-name{font-weight:700;font-size:19px;color:var(--brand-blue);white-space:nowrap}
  .divider{position:absolute;left:487px;top:54px;width:7px;height:154px;background:var(--brand-red)}
  .services{position:absolute;left:514px;top:54px;list-style:none;color:var(--brand-blue);
    font-weight:800;font-size:21px;line-height:26px;letter-spacing:.2px}
  .strip-url{color:var(--white);font-weight:700;font-size:25px;letter-spacing:1.6px}
</style>
</head>
<body>

<section class="panel side-left" aria-label="Driver side panel">
  <svg class="graphics" viewBox="0 0 952 307" preserveAspectRatio="none">
    <defs>
      <linearGradient id="photoTonesA" x1="0" y1="0" x2="1" y2="1">
        <stop offset="0" stop-color="var(--photo-dark)"/>
        <stop offset=".5" stop-color="var(--photo-light)"/>
        <stop offset="1" stop-color="var(--photo-dark)"/>
      </linearGradient>
    </defs>
    <polygon points="0,0 54,0 366,307 0,307" fill="var(--brand-blue)"/>
    <polygon points="54,0 68,0 337,268 323,268" fill="var(--brand-red)"/>
    <polygon role="img" aria-label="Photos of installed roller shutters, zipscreen blinds and sliding doors" points="76,0 270,0 534,307 370,307" fill="url(#photoTonesA)"/>
    <polygon points="478,255 952,255 952,265 487,265" fill="var(--brand-red)"/>
    <polygon points="497,265 952,265 952,307 533,307" fill="var(--brand-blue)"/>
  </svg>
  <div class="contact">
    <div class="brand-line"><span class="brand-dot"></span>Quillmere Provision Haus</div>
    <div class="phone"><svg viewBox="0 0 10 10"><path d="M2 1l2 2-1 1.3c.6 1.2 1.5 2.1 2.7 2.7L7 6l2 2-1.3 1.3C4.5 9 1 5.5.7 2.3z" fill="var(--brand-red)"/></svg>(03) 9482.1157</div>
    <div class="web">QUILLMEREPROVISIONHAUS.COM.AU</div>
  </div>
</section>

<section class="panel side-right" aria-label="Passenger side panel">
  <svg class="graphics" viewBox="0 0 952 307" preserveAspectRatio="none">
    <defs>
      <linearGradient id="photoTonesB" x1="0" y1="0" x2="1" y2="1">
        <stop offset="0" stop-color="var(--photo-dark)"/>
        <stop offset=".5" stop-color="var(--photo-light)"/>
        <stop offset="1" stop-color="var(--photo-dark)"/>
      </linearGradient>
    </defs>
    <polygon points="0,0 54,0 366,307 0,307" fill="var(--brand-blue)"/>
    <polygon points="54,0 68,0 337,268 323,268" fill="var(--brand-red)"/>
    <polygon role="img" aria-label="Photos of installed roller shutters, zipscreen blinds and sliding doors" points="76,0 270,0 534,307 370,307" fill="url(#photoTonesB)"/>
    <polygon points="478,255 952,255 952,265 487,265" fill="var(--brand-red)"/>
    <polygon points="497,265 952,265 952,307 533,307" fill="var(--brand-blue)"/>
  </svg>
  <div class="contact">
    <div class="brand-line"><span class="brand-dot"></span>Quillmere Provision Haus</div>
    <div class="phone"><svg viewBox="0 0 10 10"><path d="M2 1l2 2-1 1.3c.6 1.2 1.5 2.1 2.7 2.7L7 6l2 2-1.3 1.3C4.5 9 1 5.5.7 2.3z" fill="var(--brand-red)"/></svg>(03) 9482.1157</div>
    <div class="web">QUILLMEREPROVISIONHAUS.COM.AU</div>
  </div>
</section>

<section class="panel tailgate" aria-label="Rear panel">
  <div class="brand">
    <div class="brand-dot"></div>
    <div class="brand-name">Quillmere Provision Haus</div>
  </div>
  <div class="divider"></div>
  <ul class="services">
    <li>SECURITY DOORS</li>
    <li>ROLLER BLINDS</li>
    <li>ZIPSCREEN BLINDS</li>
    <li>ROLLER SHUTTERS</li>
    <li>AWNINGS</li>
    <li>PLANTATION SHUTTERS</li>
  </ul>
</section>

<section class="panel strip" aria-label="Windscreen strip">
  <span class="strip-url">QUILLMEREPROVISIONHAUS.COM.AU</span>
</section>

</body>
</html>
```